Business Card Design for Occupational Medicine Start Up Company

We need to design a professional business card. We are a healthcare company providing occupational medicine services to blue collar industries. We are professional, efficient and high quality service providers.

Target Market(s)

Blue Collar Industry: Shipbuilding, Ports, Trucking Companies; The Executives and Safety Officers for these companies

Industry/Entity Type

Healthcare

Contact Information for Business Card

Logo, Name, Title, Email, Phone

Other font styles liked:
• Please match our Brand Guide

Requirements
Must have
• Our Company Colors and Logo

```html
<!DOCTYPE html>
<html lang="en">
<head>
<meta charset="utf-8">
<title>CrewSafe Business Card</title>
<link rel="stylesheet" href="https://fonts.googleapis.com/css2?family=Montserrat:wght@400;500;600;700&display=swap">
<style>
  :root {
    --navy: #2e3383;
    --orange: #f4ad4f;
    --ink: #333333;
    --paper: #ffffff;
    --band: #efefef;
    --page: #ffffff;
  }
  html, body {
    margin: 0;
    padding: 0;
    width: 1200px;
    height: 2643px;
    overflow: hidden;
    background: var(--page);
    font-family: "Montserrat", sans-serif;
  }
  .sheet {
    position: relative;
    width: 1200px;
    height: 2643px;
  }
  .card {
    position: absolute;
    left: 390px;
    width: 420px;
    height: 735px;
    background: var(--paper);
    box-shadow: 0 8px 14px rgba(0,0,0,0.28);
    overflow: hidden;
  }
  .card-back { top: 546px; }
  .card-front { top: 1361px; }
  .card svg.frame {
    position: absolute;
    inset: 0;
  }
  .brand-name {
    position: absolute;
    left: 0;
    right: 0;
    text-align: center;
    color: var(--navy);
    font-weight: 700;
    letter-spacing: 1px;
  }
  .card-back .brand-name { top: 330px; font-size: 40px; }
  .card-front .brand-name { top: 140px; font-size: 30px; }
  .brand-dot {
    display: block;
    margin: 0 auto 18px;
    border-radius: 50%;
    background: var(--orange);
  }
  .card-back .brand-dot { width: 28px; height: 28px; }
  .card-front .brand-dot { width: 20px; height: 20px; margin-bottom: 12px; }
  .website {
    position: absolute;
    top: 567px;
    left: 0;
    right: 0;
    text-align: center;
    font-size: 22px;
    letter-spacing: 2px;
    color: var(--ink);
  }
  .website b { font-weight: 700; }
  .name-band {
    position: absolute;
    top: 270px;
    left: 6px;
    right: 6px;
    height: 32px;
    background: var(--band);
  }
  .person-name {
    position: absolute;
    top: 268px;
    left: 0;
    right: 0;
    text-align: center;
    font-size: 36px;
    color: var(--navy);
    font-weight: 400;
    letter-spacing: 1px;
  }
  .person-name b { font-weight: 700; }
  .person-title {
    position: absolute;
    top: 310px;
    left: 0;
    right: 0;
    text-align: center;
    font-size: 15px;
    font-weight: 700;
    color: var(--orange);
    letter-spacing: 1.2px;
  }
  .contacts {
    position: absolute;
    top: 372px;
    left: 76px;
    margin: 0;
    padding: 0;
    list-style: none;
    font-size: 17px;
    font-weight: 500;
    color: var(--ink);
    letter-spacing: 0.5px;
  }
  .contacts li {
    display: flex;
    align-items: flex-start;
    margin-bottom: 16px;
    line-height: 22px;
  }
  .contacts svg {
    width: 20px;
    height: 20px;
    flex: none;
    margin-right: 22px;
    margin-top: 1px;
  }
</style>
</head>
<body>
<main class="sheet">

  <section class="card card-back">
    <svg class="frame" width="420" height="735" viewBox="0 0 420 735">
      <polygon points="0,0 150,0 185,88 0,88" fill="var(--navy)"/>
      <polygon points="158,0 420,0 420,118 208,118" fill="var(--orange)"/>
      <polygon points="0,708 250,708 260,735 0,735" fill="var(--navy)"/>
      <polygon points="258,716 420,716 420,735 266,735" fill="var(--orange)"/>
    </svg>
    <div class="brand-name"><span class="brand-dot"></span>CREWSAFE</div>
    <div class="website">www.<b>crewsafehealth</b>.com</div>
  </section>

  <section class="card card-front">
    <svg class="frame" width="420" height="735" viewBox="0 0 420 735">
      <polygon points="0,0 262,0 254,25 0,25" fill="var(--navy)"/>
      <polygon points="270,0 420,0 420,15 265,15" fill="var(--orange)"/>
      <polygon points="0,650 185,650 145,735 0,735" fill="var(--navy)"/>
      <polygon points="210,620 420,620 420,735 155,735" fill="var(--orange)"/>
    </svg>
    <div class="brand-name"><span class="brand-dot"></span>CREWSAFE</div>
    <div class="name-band"></div>
    <div class="person-name"><b>DANA</b> MORROW</div>
    <div class="person-title">CHIEF EXECUTIVE OFFICER</div>
    <ul class="contacts">
      <li>
        <svg viewBox="0 0 20 20"><path d="M5 2 L8 6 L6 8 Q8 12 12 14 L14 12 L18 15 L16 18 Q8 18 2 6 Z" fill="none" stroke="var(--orange)" stroke-width="1.8"/></svg>
        +1 (555) 013-2048
      </li>
      <li>
        <svg viewBox="0 0 20 20"><rect x="2" y="5" width="16" height="11" fill="var(--orange)"/><path d="M2 5 L10 11 L18 5" fill="none" stroke="#fff" stroke-width="1.4"/></svg>
        info@crewsafehealth.com
      </li>
      <li>
        <svg viewBox="0 0 20 20"><path d="M10 19 Q3 11 3 8 A7 7 0 0 1 17 8 Q17 11 10 19 Z" fill="var(--orange)"/><circle cx="10" cy="8" r="2.6" fill="#fff"/></svg>
        <span>Harbor Lane 410, 3rd<br>Floor Port City -<br>United State</span>
      </li>
      <li>
        <svg viewBox="0 0 20 20"><circle cx="10" cy="10" r="8" fill="none" stroke="var(--orange)" stroke-width="1.6"/><ellipse cx="10" cy="10" rx="3.5" ry="8" fill="none" stroke="var(--orange)" stroke-width="1.4"/><line x1="2" y1="10" x2="18" y2="10" stroke="var(--orange)" stroke-width="1.4"/></svg>
        www.crewsafehealth.com
      </li>
    </ul>
  </section>

</main>
</body>
</html>
```